Vexo Systems Web Site Design

Need a basic site to show clients a little about what we do. We are a custom audio video company in the high-end residential market. Need a few basic but professional pages to show past projects and products we sell. No e-commerce. Should include my new logo from ArtHivePro.

Industry/Entity Type

Residential

Number of Pages Required

2 page

Font styles to use
Serif
Sans Serif

Colors
f78f20

Requirements
Must have
• Company Logo, Send feedback page
Nice to have
• I have no ideas about design, but I do know what I like and dislike when I see it.

```html
<!DOCTYPE html>
<html lang="en">
<head>
<meta charset="utf-8">
<title>Vexo Systems</title>
<link href="https://fonts.googleapis.com/css2?family=Lato:wght@400;700&family=Oxygen:wght@300;400&display=swap" rel="stylesheet">
<style>
:root{
  --orange:#f78f20;
  --ink:#1c1c1c;
  --text:#333;
  --rule:#cfcfcf;
  --footer:#262626;
  --white:#fff;
}
*{margin:0;padding:0;box-sizing:border-box}
html,body{width:870px;height:1200px;overflow:hidden;background:var(--white)}
body{position:relative;font-family:'Lato',sans-serif;color:var(--text)}
.abs{position:absolute}

/* header */
.site-header{left:0;top:0;width:870px;height:88px;background:var(--white)}
.brand{left:94px;top:24px;display:flex;align-items:center;gap:10px}
.brand-mark{width:30px;height:30px;border-radius:50%;background:var(--orange)}
.brand-name{font-family:'Oxygen',sans-serif;font-size:24px;font-weight:400;color:var(--ink);letter-spacing:.5px}
.call{left:652px;top:9px;display:flex;align-items:center;gap:8px}
.call-label{font-size:9.5px;letter-spacing:1.6px;font-weight:700;color:var(--ink)}
.call-number{font-size:14px;color:var(--ink);margin-top:1px}
.main-nav{right:94px;top:60px;display:flex;align-items:center;font-size:9.5px;font-weight:700;color:var(--ink)}
.main-nav span{padding:0 11px;border-left:1px solid #bbb;line-height:14px}
.main-nav .home{border:none;padding:0 11px 0 0;display:flex}

/* hero */
.hero{left:0;top:88px;width:870px;height:354px;background:linear-gradient(180deg,#5a1518 0%,#7d2226 40%,#3a0f10 75%,#1b1212 100%)}
.hero-arrow{top:158px;width:34px;height:34px;border-radius:50%;border:1.5px solid rgba(255,255,255,.55)}
.hero-caption{left:0;top:312px;width:870px;height:42px;background:rgba(20,20,20,.72);color:var(--white);font-family:'Oxygen',sans-serif;font-size:20px;font-weight:300;text-align:center;line-height:42px}

/* sections */
.section-title{left:0;width:870px;text-align:center;font-family:'Oxygen',sans-serif;font-weight:300;font-size:20px;color:var(--ink);letter-spacing:.3px}
.divider{left:170px;width:530px;height:12px}
.divider .line{position:absolute;top:6px;height:1px;width:250px;background:var(--rule)}
.divider .dot{position:absolute;left:259px;top:0;width:12px;height:12px;border-radius:50%;background:var(--orange)}
.intro{left:96px;top:524px;width:678px;text-align:center;font-size:11px;line-height:17.6px;color:var(--text)}
.btn{left:380px;top:594px;width:110px;height:26px;border-radius:5px;background:var(--ink);color:var(--white);font-size:11px;font-weight:700;text-align:center;line-height:26px}

.services{left:0;top:658px;width:870px;height:267px;background:var(--orange)}
.services .section-title{top:30px}
.services .divider .line{background:var(--ink)}
.services .divider .dot{background:var(--ink)}
.service{top:102px;width:162px;text-align:center}
.service-icon{display:block;margin:0 auto;width:86px;height:86px}
.service-name{margin-top:12px;font-family:'Oxygen',sans-serif;font-size:13.5px;line-height:18px;color:var(--ink)}
.col-rule{top:102px;width:1px;height:132px;background:rgba(0,0,0,.15)}

.project{top:1017px;width:157px;height:111px}
.project-caption{display:flex;align-items:center;justify-content:center;text-align:center;color:var(--white);font-family:'Oxygen',sans-serif;font-size:13.5px;line-height:18px;padding:0 20px}

.site-footer{left:0;top:1163px;width:870px;height:37px;background:var(--footer);color:#ddd;font-size:10px;text-align:center;line-height:37px}
</style>
</head>
<body>

<header class="site-header abs">
  <div class="brand abs">
    <div class="brand-mark"></div>
    <div class="brand-name">Vexo Systems</div>
  </div>
  <div class="call abs">
    <svg width="28" height="28" viewBox="0 0 28 28"><circle cx="14" cy="14" r="12.5" fill="none" stroke="#f78f20" stroke-width="2"/><path d="M9 8c1-1 2-1 3 0l1.5 2.5c.4.8 0 1.5-.7 2l-.8.6c.8 1.7 2 3 3.7 3.9l.6-.8c.5-.7 1.3-1 2-.6L21 17c1 .7 1 1.8 0 3-2 2-6 0-8.5-2.5S7 10 9 8z" fill="#f78f20"/></svg>
    <div>
      <div class="call-label">CALL US TODAY</div>
      <div class="call-number">555 204 3187</div>
    </div>
  </div>
  <nav class="main-nav abs">
    <span class="home"><svg width="13" height="12" viewBox="0 0 13 12"><path d="M6.5 0L13 6h-2v6H8V8H5v4H2V6H0z" fill="#f78f20"/></svg></span>
    <span>ABOUT US</span>
    <span>PRODUCT &amp; SERVICES</span>
    <span>PAST PROJECTS</span>
    <span>FEEDBACK</span>
    <span>CONTACT US</span>
  </nav>
</header>

<section class="hero abs" role="img" aria-label="Photo of a home cinema room with red walls, a projection screen and leather recliners">
  <div class="hero-arrow abs" style="left:41px"><svg width="31" height="31" viewBox="0 0 31 31"><path d="M18 8l-7 7.5 7 7.5" fill="none" stroke="#fff" stroke-width="1.5"/></svg></div>
  <div class="hero-arrow abs" style="left:795px"><svg width="31" height="31" viewBox="0 0 31 31"><path d="M13 8l7 7.5-7 7.5" fill="none" stroke="#fff" stroke-width="1.5"/></svg></div>
  <div class="hero-caption abs">We are a custom audio video company in the high-end residential market</div>
</section>

<h1 class="section-title abs" style="top:470px">WELCOME TO VEXO SYSTEMS</h1>
<div class="divider abs" style="top:502px"><div class="line" style="left:0"></div><div class="dot"></div><div class="line" style="left:280px"></div></div>
<p class="intro abs">Lorem ipsum dolor sit amet, consectetuer adipiscing elit, sed diam nonummy nibh euismod tincidunt ut laoreet dolore magna aliquam erat volutpat. Ut wisi enim ad minim veniam, quis nostrud exerci tation ullamcorper suscipit lobortis nisl ut aliquip ex ea commodo consequat. Duis autem vel eum iriure dolor in hendrerit in vulputate velit esse molestie consequat, vel illum dolore eu feugiat nulla facilisis at vero.</p>
<div class="btn abs">READ MORE</div>

<section class="services abs">
  <h2 class="section-title abs">PRODUCT &amp; SERVICES</h2>
  <div class="divider abs" style="top:63px"><div class="line" style="left:0"></div><div class="dot"></div><div class="line" style="left:280px"></div></div>
  <svg class="abs" style="left:58px;top:145px" width="26" height="46" viewBox="0 0 26 46"><path d="M24 1L2 23l22 22" fill="none" stroke="#1c1c1c" stroke-width="1.2"/></svg>
  <svg class="abs" style="left:786px;top:145px" width="26" height="46" viewBox="0 0 26 46"><path d="M2 1l22 22L2 45" fill="none" stroke="#1c1c1c" stroke-width="1.2"/></svg>

  <div class="service abs" style="left:111px">
    <svg class="service-icon" viewBox="0 0 86 86"><circle cx="43" cy="43" r="41" fill="none" stroke="#1c1c1c" stroke-width="3"/><rect x="25" y="33" width="36" height="26" rx="4" fill="none" stroke="#1c1c1c" stroke-width="4"/><path d="M35 33l-5-7M51 33l4-7" stroke="#1c1c1c" stroke-width="2.5"/><rect x="49" y="38" width="7" height="16" fill="#1c1c1c"/></svg>
    <div class="service-name">DISTRIBUTED<br>VIDEO</div>
  </div>
  <div class="col-rule abs" style="left:273px"></div>
  <div class="service abs" style="left:273px">
    <svg class="service-icon" viewBox="0 0 86 86"><circle cx="43" cy="43" r="41" fill="none" stroke="#1c1c1c" stroke-width="3"/><circle cx="43" cy="43" r="20" fill="none" stroke="#1c1c1c" stroke-width="4"/><path d="M37 32l14 11-14 11z" fill="#1c1c1c"/></svg>
    <div class="service-name">MEDIA<br>ROOMS</div>
  </div>
  <div class="col-rule abs" style="left:435px"></div>
  <div class="service abs" style="left:435px">
    <svg class="service-icon" viewBox="0 0 86 86"><circle cx="43" cy="43" r="41" fill="none" stroke="#1c1c1c" stroke-width="3"/><path d="M43 24L22 44h6v17h11V51h8v10h11V44h6z" fill="#1c1c1c"/></svg>
    <div class="service-name">RESIDENTIAL<br>CINEMAS</div>
  </div>
  <div class="col-rule abs" style="left:597px"></div>
  <div class="service abs" style="left:597px">
    <svg class="service-icon" viewBox="0 0 86 86"><circle cx="43" cy="43" r="41" fill="none" stroke="#1c1c1c" stroke-width="3"/><rect x="36" y="22" width="12" height="34" rx="3" transform="rotate(-25 42 39)" fill="#1c1c1c"/><circle cx="40" cy="30" r="1.6" fill="#f78f20" transform="rotate(-25 42 39)"/><circle cx="44" cy="30" r="1.6" fill="#f78f20" transform="rotate(-25 42 39)"/></svg>
    <div class="service-name">WHOLE-HOUSE<br>CONTROL SYSTEMS</div>
  </div>
</section>

<h2 class="section-title abs" style="top:954px">PAST PROJECTS</h2>
<div class="divider abs" style="top:987px"><div class="line" style="left:0"></div><div class="dot"></div><div class="line" style="left:280px"></div></div>
<svg class="abs" style="left:58px;top:1050px" width="26" height="46" viewBox="0 0 26 46"><path d="M24 1L2 23l22 22" fill="none" stroke="#1c1c1c" stroke-width="1.2"/></svg>
<svg class="abs" style="left:786px;top:1050px" width="26" height="46" viewBox="0 0 26 46"><path d="M2 1l22 22L2 45" fill="none" stroke="#1c1c1c" stroke-width="1.2"/></svg>

<div class="project project-caption abs" style="left:94px;background:linear-gradient(180deg,#8a1a1a,#5a0e0e)" role="img" aria-label="Project photo of a red home theatre room">Lorem ipsum dolor sit amet</div>
<div class="project abs" style="left:269px;background:linear-gradient(90deg,#6f6a4e,#8c8766)" role="img" aria-label="Project photo of a hand-held remote beside a wall keypad"></div>
<div class="project abs" style="left:444px;background:linear-gradient(135deg,#5a5a5a,#111)" role="img" aria-label="Project photo of loudspeakers"></div>
<div class="project abs" style="left:619px;background:linear-gradient(180deg,#9cc0de,#6d8a5a)" role="img" aria-label="Project photo of an outdoor television by a sports court"></div>

<footer class="site-footer abs">Copyright © 2015 VEXO SYSTEMS. All Rights Reserved</footer>

</body>
</html>
```